Atelier Marrow Architecture business card

We need to update our business card. We do high end custom residential, hospitality, and wellness architecture. We focus on creating unique spaces and design around the five senses, believing that architecture's true impact is not on our surroundings, but within us. We would like to see designs are instill a sense of calm awe. They should be crisp, fresh, clean, authentic, & contemporary without being sterile, overworked, or harsh. White space is important. Alternative materials are an option if natural. We have created our own logo and would like designs to incorporate it. However, we are willing to see alternatives if the logo becomes a stumbling block and you have an alternate you suggest. Card must have the following information:
Atelier Marrow Architecture, Inc.
728 Holloway Ct. NE Atlanta, GA 30318
Marcus T. Whitcombe, AIA, NCARB, LEED AP BD+C
ateliermarrow.example

Target Market(s)

Higher net worth individuals with an appreciation for design, nature, sustainability,

Industry/Entity Type

Architect

Contact Information for Business Card

See above. The title of Owner or Architect is helpful but not necessary. Minimalism should trump additional information.

Font styles to use
Serif
Sans Serif

Requirements
Must have
• It should look professional. It must use logo
Should not have
• caligraphy, animals, anything that is cute,

```html
<!DOCTYPE html>
<html lang="en">
<head>
<meta charset="utf-8">
<title>Atelier Marrow Architecture – Business Card</title>
<link href="https://fonts.googleapis.com/css2?family=Source+Sans+3:wght@400;600&display=swap" rel="stylesheet">
<style>
  :root {
    --backdrop: #161616;
    --card-front: #f3f3f3;
    --card-back: #ffffff;
    --brand-green: #127312;
    --ink: #1d1d1d;
  }
  * { box-sizing: border-box; margin: 0; padding: 0; }
  html, body {
    width: 1200px;
    height: 900px;
    overflow: hidden;
  }
  body {
    position: relative;
    background: var(--backdrop);
    font-family: "Source Sans 3", "Myriad Pro", Arial, sans-serif;
    color: var(--ink);
  }
  .card {
    position: absolute;
    top: 184px;
    height: 490px;
    border-radius: 12px;
  }
  .card--front {
    left: 299px;
    width: 301px;
    background: var(--card-front);
  }
  .card--back {
    left: 645px;
    width: 305px;
    background: var(--card-back);
  }
  .wordmark {
    position: absolute;
    left: 0;
    right: 0;
    display: flex;
    align-items: center;
    justify-content: center;
    gap: 9px;
  }
  .card--front .wordmark { top: 128px; }
  .card--back .wordmark { top: 238px; }
  .wordmark__square {
    width: 14px;
    height: 14px;
    background: var(--brand-green);
    flex: none;
  }
  .wordmark__name {
    font-size: 17px;
    font-weight: 600;
    color: var(--brand-green);
    white-space: nowrap;
  }
  .contact {
    position: absolute;
    top: 256px;
    left: 0;
    right: 0;
    text-align: center;
    font-size: 13.5px;
    line-height: 17.5px;
  }
  .contact__name {
    font-size: 17px;
    font-weight: 600;
    color: var(--brand-green);
    line-height: 20px;
  }
  .contact__block { margin-top: 12px; }
</style>
</head>
<body>
  <section class="card card--front" aria-label="Card front">
    <div class="wordmark">
      <span class="wordmark__square"></span>
      <span class="wordmark__name">Atelier Marrow Architecture</span>
    </div>
    <div class="contact">
      <p class="contact__name">Marcus T. Whitcombe</p>
      <p class="contact__credentials">AIA, NCARB, LEED AP BD+C</p>
      <p class="contact__block">728 Holloway Ct. NE Atlanta,<br>GA 30318</p>
      <p class="contact__block">044-555 010 246<br>info@ateliermarrow.example<br>www.ateliermarrow.example</p>
    </div>
  </section>

  <section class="card card--back" aria-label="Card back">
    <div class="wordmark">
      <span class="wordmark__square"></span>
      <span class="wordmark__name">Atelier Marrow Architecture</span>
    </div>
  </section>
</body>
</html>
```